Professional, Elegant, Modern and Playful stationery design for an Orthodontist (Dentist)

We need a new stationery design for an Orthodontist (Dentist).
We would like to see designs that are elegant, but also playful. The designs and colors should be in harmony with the existing logo (uploaded).
The font of the logo text is roboto (Google), you don't need to use the same font, but the used font has to be in harmony with the font used in the logo and it has to be usable in Microsoft Word.
The colors used have to be in harmony with the logo.
The design for following parts are needed:
- A4 letter paper design
- A4 Microsoft Word Template (with and without letterhead)
- Envelope designs for C4 and C5 with the window on the right side
- CD/DVD-label design
- Stamping design

Target Market(s)

Orthodontist (Dentist)

Industry/Entity Type

It Professional

Font styles to use
Sans Serif

Colors

Designer to choose colors to be used in the design.

Requirements
Must have
• * Logo files are uploaded
• * A4 letter paper design: for printing press
• - Address position is on the right side
• - Needed Information in the letterhead:
• - Logo with company name as a unit
• or
• - separate the logo from the text and position them separately
• - Text needed:
• Kieferorthopädie Wendelau
• Dr. med. dent. Lukas Brenner
• Fachzahnarzt für Kieferorthopädie (CH)
• Eidg. dipl. Zahnarzt, Mitglied VZB und FDT
• Hagelbachweg 14
• 8907 Schlieren
• 044 512 37 90
• (fax:)
• 044 512 37 91
• info@wendelau-praxis.net
• www.wendelau-praxis.net
• * A4 Microsoft Word Templates:
• - an empty and undesigned text example template is uploaded
• - the address lines are already correctly positioned behind the envelope window
• - design the positions of all elements
• - choose suitable fonts, which are in harmony with the font in the logo and the letterhead and which can be used in Microsoft Word (compatible with latest version, no old versions (.doc) needed)
• - choose suitable font sizes weights and colors, which are in harmony with the font in the logo and the letterhead.
• - One version with letterhead for printing on an empty paper
• - One version without letterhead for printing on a paper with letterhead already printed in printing press
• * Envelopes C4 and C5
• - window on the right side
• - Logo with company name (see uploaded files) as a unit
• or
• - Text needed:
• Hagelbachweg 14
• 8907 Schlieren
• * DVD/CD-label:
• or
• - Text needed:
• Hagelbachweg 14
• 8907 Schlieren
• 044 512 37 90
• info@wendelau-praxis.net
• www.wendelau-praxis.net
• - Patient name with birth date:
• Doe John, *1.2.1999
• - Two lines of text describing the contents on the CD/DVD
• * Stamping design:
• - Logo
• - Text:
• Kieferorthopädie Wendelau GmbH
• Hagelbachweg 14
• 8907 Schlieren
Nice to have
• -
Should not have
• - Old Microsoft Word versions (.doc)

```html
<!DOCTYPE html>
<html lang="de">
<head>
<meta charset="utf-8">
<title>Kieferorthopädie Wendelau – CD-Label</title>
<link rel="stylesheet" href="https://fonts.googleapis.com/css2?family=Open+Sans:ital,wght@0,400;0,700;1,400&display=swap">
<style>
  :root {
    --page-bg: #b7c6ef;
    --ring-blue: #1f67a8;
    --ring-dark: #3a3f4a;
    --label-light: #f3f7fb;
    --label-tint: #dfe8f3;
    --brand-navy: #17167a;
    --brand-sky: #2a9bd8;
    --text-grey: #6a6d73;
    --line-grey: #6b6e74;
  }
  html, body {
    margin: 0;
    padding: 0;
    width: 1200px;
    height: 857px;
    overflow: hidden;
    background: var(--page-bg);
  }
  .cd-label {
    display: block;
    width: 1200px;
    height: 857px;
    font-family: "Open Sans", sans-serif;
  }
  .practice-name { font-weight: 700; font-size: 30px; fill: var(--brand-navy); }
  .practice-detail { font-size: 18px; fill: var(--text-grey); }
  .field-label { font-size: 16px; font-style: italic; fill: var(--brand-navy); }
  .field-line { stroke: var(--line-grey); stroke-width: 1.2; }
  .rim-contact { font-size: 17px; fill: var(--text-grey); }
  .rim-bullet { fill: var(--brand-navy); }
</style>
</head>
<body>
<svg class="cd-label" viewBox="0 0 1200 857" xmlns="http://www.w3.org/2000/svg" aria-label="CD-Label Kieferorthopädie Wendelau">
  <defs>
    <radialGradient id="label-fill" cx="50%" cy="45%" r="60%">
      <stop offset="0%" stop-color="var(--label-light)"/>
      <stop offset="100%" stop-color="var(--label-tint)"/>
    </radialGradient>
    <path id="rim-arc" d="M 240 428 A 360 360 0 0 0 960 428"/>
  </defs>

  <!-- disc edge and blue ring -->
  <circle class="disc-edge" cx="600" cy="428" r="402" fill="var(--ring-dark)"/>
  <circle class="disc-ring" cx="600" cy="428" r="396" fill="var(--ring-blue)"/>
  <circle class="disc-surface" cx="600" cy="428" r="388" fill="url(#label-fill)"
          role="img" aria-label="Dezentes helles Hintergrundmuster aus blassblauen Quadraten"/>

  <!-- practice name mark -->
  <g class="brand-block">
    <circle cx="408" cy="150" r="12" fill="var(--brand-sky)"/>
    <text class="practice-name" x="432" y="161">Kieferorthopädie Wendelau</text>
    <text class="practice-detail" x="432" y="196">Dr. med. dent. Lukas Brenner</text>
    <text class="practice-detail" x="432" y="222">Fachzahnarzt für Kieferorthopädie (CH)</text>
    <text class="practice-detail" x="432" y="248">Eidg. dipl. Zahnarzt, Mitglied VZB und FDT</text>
  </g>

  <!-- centre hole -->
  <circle class="hub-clear" cx="600" cy="428" r="72" fill="#e9eef5" stroke="#cfd8e4" stroke-width="2"/>
  <circle class="hub-hole" cx="600" cy="428" r="44" fill="var(--page-bg)" stroke="#9aa8c8" stroke-width="3"/>

  <!-- patient fields -->
  <g class="patient-fields">
    <text class="field-label" x="330" y="540">Patient Name:</text>
    <line class="field-line" x1="442" y1="540" x2="870" y2="540"/>
    <text class="field-label" x="330" y="582">D.O.B.:</text>
    <line class="field-line" x1="392" y1="582" x2="870" y2="582"/>
    <line class="field-line" x1="330" y1="624" x2="870" y2="624"/>
  </g>

  <!-- contact details along the rim -->
  <text class="rim-contact">
    <textPath href="#rim-arc" startOffset="50%" text-anchor="middle"><tspan class="rim-bullet">● </tspan>Hagelbachweg 14, 8907 Schlieren  <tspan class="rim-bullet">● </tspan>044 512 37 90  <tspan class="rim-bullet">● </tspan>044 512 37 91  <tspan class="rim-bullet">● </tspan>info@wendelau-praxis.net  <tspan class="rim-bullet">● </tspan>www.wendelau-praxis.net</textPath>
  </text>
</svg>
</body>
</html>
```